Help design website for "Verdant Harbor Advisory" to advance the common good

Here is the Google doc link that lays out the design:

https://files.quillmarsh.net/doc/7TrWbnQe48XkLpZa2uMvYcD0sHfGjR35NwoEi9KxyBt/view?mode=share

Here is the Google drive folder with the logos and photos: https://store.quillmarsh.net/open?id=4K9pRtLmWqZx8825BvNcUaYeHs3Jd

The testimonials are being gathered and will be shared by Friday, 1/4.

The winner will also have to migrate the coding files to my hosting site.

Thank you for your help! Looking forward to seeing your designs.

Target Market(s)

Prospective clients

Industry/Entity Type

Non Profit

Coding

Coded - Design and coding required

Number of Pages Required

5+ page

Requirements
Must have
• Noted in the Google doc regarding layout.
Nice to have

```html
<!DOCTYPE html>
<html lang="en">
<head>
<meta charset="utf-8">
<title>Verdant Harbor Advisory</title>
<link href="https://fonts.googleapis.com/css2?family=Montserrat:wght@400;500;600;700&family=Open+Sans:wght@400;600;700&display=swap" rel="stylesheet">
<style>
:root{
  --blue:#5a80be;
  --blue-deep:#3e66a8;
  --blue-soft:#8faad6;
  --blue-pale:#dfe7f3;
  --navy:#2b3a5c;
  --ink:#3a3f4b;
  --muted:#6b7180;
  --line:#d9dee7;
  --paper:#ffffff;
  --grey:#f4f5f7;
}
*{box-sizing:border-box;margin:0;padding:0}
html,body{width:1200px;height:5000px;overflow:hidden;background:var(--paper)}
body{font-family:"Open Sans",Arial,sans-serif;color:var(--ink);position:relative}
.abs{position:absolute}
h2.section-title{position:absolute;left:0;width:1200px;text-align:center;font-family:"Montserrat",Arial,sans-serif;font-weight:700;font-size:30px;letter-spacing:1px;color:var(--navy);text-transform:uppercase}
h2.section-title span{color:var(--blue)}
h2.section-title.light{color:#fff}
h2.section-title.light span{color:#fff}

/* header */
.site-header{position:absolute;left:0;top:0;width:1200px;height:150px;background:var(--blue);display:flex;align-items:center;justify-content:space-between;padding:0 70px;z-index:2}
.brand{display:flex;align-items:center;gap:16px;color:#fff;font-family:"Montserrat",Arial,sans-serif}
.brand-square{width:40px;height:40px;border:3px solid #fff}
.brand-name{font-size:24px;font-weight:600;letter-spacing:1px;line-height:1.2}
.main-nav{display:flex;gap:40px;font-family:"Montserrat",Arial,sans-serif;font-weight:600;font-size:15px;color:#fff;text-transform:uppercase;letter-spacing:.5px}

/* hero */
.hero{position:absolute;left:0;top:150px;width:1200px;height:435px;clip-path:polygon(0 0,100% 0,100% 72%,50% 100%,0 72%);background:linear-gradient(180deg,#3a4a63 0%,#6b7c95 35%,#a9b3c4 60%,#7f8ea6 100%)}
.hero-arrow{position:absolute;top:290px;width:34px;height:44px;background:rgba(20,28,45,.75);display:flex;align-items:center;justify-content:center;z-index:3}
.hero-edge{position:absolute;left:0;top:150px;width:1200px;height:445px;clip-path:polygon(0 0,100% 0,100% 71%,50% 100%,0 71%);background:var(--blue-soft);z-index:0}

/* about */
.about-photo{left:95px;top:795px;width:275px;height:275px;border-radius:50%;background:radial-gradient(circle at 50% 40%,#c8b4a6,#6e7f99 70%);border:8px solid #e9eef6;box-shadow:0 0 0 3px var(--blue-soft)}
.about-copy{left:480px;top:800px;width:650px;font-size:15.5px;line-height:1.55;color:var(--ink)}
.about-copy p+p{margin-top:18px}
.about-rule{left:0;top:1235px;width:1200px;height:1px;background:var(--line)}

/* work history */
.partner-grid{left:155px;top:1425px;width:890px;display:grid;grid-template-columns:repeat(3,270px);gap:40px 40px}
.partner{height:128px;background:#fff;border-radius:6px;box-shadow:0 3px 14px rgba(40,60,100,.14);display:flex;align-items:center;justify-content:center;gap:12px;font-family:"Montserrat",Arial,sans-serif;font-weight:700;font-size:18px;color:var(--navy);text-align:center;padding:0 18px}
.partner i{width:22px;height:22px;background:var(--blue);flex:none}

/* services */
.services{left:0;top:1800px;width:1200px;height:870px;clip-path:polygon(0 0,100% 0,100% 84%,50% 100%,0 84%);background:linear-gradient(120deg,#6f8fc4 0%,#8aa6d2 45%,#5f82bd 100%)}
.services-lead{left:0;top:1988px;width:1200px;text-align:center;color:#fff;font-size:20px;font-style:italic;font-weight:600}
.service-card{top:2060px;width:335px;height:280px;background:rgba(255,255,255,.18);border:1px solid rgba(255,255,255,.55);border-radius:6px;padding:26px 22px;color:#fff}
.service-card h3{font-size:14px;font-weight:700;margin:18px 0 4px}
.service-card p{font-size:13.5px;line-height:1.45}
.service-links{position:absolute;left:22px;bottom:22px;display:flex;gap:28px;font-size:13.5px;font-weight:600}
.service-links span{display:flex;align-items:center;gap:8px}
.slide-arrow{top:2470px;width:90px;height:30px;border:1px solid rgba(255,255,255,.8);border-radius:15px;display:flex;align-items:center;justify-content:center}

/* media */
.media-lead{left:0;top:2848px;width:1200px;text-align:center;font-size:18px;font-weight:600;color:var(--ink)}
.media-card{top:2925px;width:335px;height:400px;background:#fff;border-radius:6px;box-shadow:0 3px 16px rgba(40,60,100,.15);padding:22px 22px}
.media-head{display:flex;justify-content:center;align-items:center;gap:14px;font-family:"Montserrat",Arial,sans-serif;font-weight:600;font-size:19px;color:var(--navy);border-bottom:1px solid var(--line);padding-bottom:16px}
.media-body{font-size:14.5px;line-height:1.45;margin-top:18px;min-height:66px}
.media-body b{display:block}
.media-visual{height:128px;margin-top:10px}
.play-btn{position:absolute;left:139px;top:72px;width:54px;height:54px;border-radius:50%;border:2px solid #fff;background:rgba(30,40,60,.45);display:flex;align-items:center;justify-content:center}
.load-more{position:absolute;left:0;bottom:26px;width:100%;display:flex;justify-content:center;align-items:center;gap:12px;color:var(--blue);font-size:15px;font-weight:600}

/* contact */
.contact-band{left:0;top:3425px;width:1200px;height:380px;background:var(--grey)}
.contact-item{font-size:16px;line-height:1.5;color:var(--ink)}
.contact-item b{display:block;color:var(--navy)}

/* message */
.message{left:0;top:3795px;width:1200px;height:690px;clip-path:polygon(0 8%,100% 0,100% 88%,50% 100%,0 88%);background:linear-gradient(110deg,#7e9ccd 0%,#9ab2da 45%,#6d8dc4 100%)}
.field{position:absolute;height:46px;background:rgba(255,255,255,.35);border:1px solid rgba(255,255,255,.6);color:#fff;font-size:14px;padding:12px 16px}
.send-btn{left:485px;top:4275px;width:230px;height:48px;border:2px solid #fff;border-radius:4px;color:#fff;font-family:"Montserrat",Arial,sans-serif;font-weight:600;font-size:15px;display:flex;align-items:center;justify-content:center;background:rgba(255,255,255,.12)}

/* footer */
.footer-brand{left:0;top:4560px;width:1200px;display:flex;justify-content:center;align-items:center;gap:16px;font-family:"Montserrat",Arial,sans-serif;color:var(--navy)}
.footer-brand .brand-square{border-color:var(--navy)}
.footer-col{top:4690px;font-size:13.5px;line-height:1.55;color:var(--ink)}
.footer-col h4{font-family:"Montserrat",Arial,sans-serif;font-size:14px;font-weight:700;color:var(--blue-deep);text-transform:uppercase;border-bottom:1px solid var(--line);padding-bottom:8px;margin-bottom:12px}
.footer-col .row{display:flex;align-items:flex-start;gap:10px;margin-bottom:14px}
.newsletter{display:flex;margin-top:4px}
.newsletter div:first-child{width:160px;height:38px;border:1px solid var(--line);font-size:12.5px;padding:10px;color:var(--muted)}
.newsletter div:last-child{width:95px;height:38px;background:var(--blue);color:#fff;font-size:12.5px;font-weight:700;display:flex;align-items:center;justify-content:center}
.copyright{left:0;top:4955px;width:1200px;height:45px;border-top:1px solid var(--line);font-size:12px;font-weight:700;color:var(--navy);padding:14px 25px}
</style>
</head>
<body>

<header class="site-header">
  <div class="brand">
    <div class="brand-square"></div>
    <div class="brand-name">Verdant Harbor Advisory</div>
  </div>
  <nav class="main-nav">
    <span>About</span><span>Services &amp; Testimonials ⌄</span><span>Media &amp; Impact ⌄</span><span>Contact</span>
  </nav>
</header>

<div class="hero-edge"></div>
<div class="hero" role="img" aria-label="Photo of a speaker on stage addressing a large seated audience in a gymnasium"></div>
<div class="hero-arrow" style="left:0"><svg width="14" height="20" viewBox="0 0 14 20"><path d="M11 2 3 10l8 8" stroke="#fff" stroke-width="3" fill="none"/></svg></div>
<div class="hero-arrow" style="right:0"><svg width="14" height="20" viewBox="0 0 14 20"><path d="M3 2l8 8-8 8" stroke="#fff" stroke-width="3" fill="none"/></svg></div>

<h2 class="section-title" style="top:705px">About <span>Verdant Harbor</span></h2>
<div class="abs about-photo" role="img" aria-label="Portrait photo of founder Dana Whitfield"></div>
<div class="abs about-copy">
  <p>Verdant Harbor Advisory supports nonprofit organizations and educational institutions to carry out their missions to benefit the wider community.</p>
  <p>Founder Dana Whitfield is an educator with a 22-year record of demonstrated achievement and leadership roles in nonprofits and educational institutions. Most recently, she served as Associate Dean of Students in the University and Director of the Lakeview Service Center at Lakeview University. Dana has designed, implemented, and evaluated community-based learning and leadership training programs that have attained positive outcomes documented by survey results, recognition by outside agencies, and grants awarded for new initiatives and expansions. She has also significantly and consistently increased the number of program applicants, volunteers, and community partnerships through innovative programming, improved reputation, targeted recruitment, marketing and communications.</p>
</div>
<div class="abs about-rule"></div>

<h2 class="section-title" style="top:1337px">Work <span>History</span></h2>
<div class="abs partner-grid">
  <div class="partner"><i></i>Lakeview Service Center</div>
  <div class="partner"><i></i>Meridian Fellows</div>
  <div class="partner"><i></i>Brightpath Bay Schools</div>
  <div class="partner"><i></i>Civic Youth Labs</div>
  <div class="partner"><i></i>ServeNation Corps</div>
  <div class="partner"><i></i>Harborline Exchange</div>
</div>

<div class="abs services" role="img" aria-label="Blue-tinted photo of a facilitator leading a group session"></div>
<h2 class="section-title light" style="top:1905px">Services <span>&amp; Testimonials</span></h2>
<div class="abs services-lead">Dana offers consulting services in six areas to support nonprofits and educational institutions.</div>

<div class="abs service-card" style="left:73px">
  <svg width="44" height="30" viewBox="0 0 44 30" fill="#fff"><circle cx="10" cy="8" r="5"/><circle cx="22" cy="6" r="6"/><circle cx="34" cy="8" r="5"/><path d="M2 28c0-8 5-12 8-12s8 4 8 12zM13 28c0-10 5-14 9-14s9 4 9 14zM26 28c0-8 5-12 8-12s8 4 8 12z"/></svg>
  <h3>Staff Professional Development</h3>
  <p>Dana has supervised, coached, and mentored hundreds of staff members, including professionals and students. She uses the "scaffold model coach field" approach to empower and guide her staff in their personal and professional growth.</p>
  <div class="service-links"><span>→ Learn More</span><span>◌ Testimonials</span></div>
</div>
<div class="abs service-card" style="left:433px">
  <svg width="44" height="30" viewBox="0 0 44 30" fill="none" stroke="#fff" stroke-width="2"><circle cx="12" cy="9" r="5"/><circle cx="32" cy="9" r="5"/><path d="M4 28c0-7 4-11 8-11s8 4 8 11M24 28c0-7 4-11 8-11s8 4 8 11"/></svg>
  <h3>Community Partnership Development</h3>
  <p>Dana has collaborated with more than 200 nonprofits, schools, government agencies, and businesses with corporate social responsibility units to create mutually beneficial partnerships.</p>
  <div class="service-links"><span>→ Learn More</span><span>◌ Testimonials</span></div>
</div>
<div class="abs service-card" style="left:793px">
  <svg width="44" height="30" viewBox="0 0 44 30" fill="#fff"><circle cx="8" cy="10" r="4"/><circle cx="18" cy="10" r="4"/><circle cx="28" cy="10" r="4"/><circle cx="38" cy="10" r="4"/><rect x="5" y="16" width="6" height="13"/><rect x="15" y="16" width="6" height="13"/><rect x="25" y="16" width="6" height="13"/><rect x="35" y="16" width="6" height="13"/></svg>
  <h3>Group Facilitation &amp; Leadership Training</h3>
  <p>Dana has facilitated student groups, experiential learning activities, and dialogues on social justice issues, such as power and privilege, education, and poverty.</p>
  <div class="service-links"><span>→ Learn More</span><span>◌ Testimonials</span></div>
</div>
<div class="abs slide-arrow" style="left:75px"><svg width="40" height="12" viewBox="0 0 40 12"><path d="M38 6H3m5-5L3 6l5 5" stroke="#fff" stroke-width="1.6" fill="none"/></svg></div>
<div class="abs slide-arrow" style="left:1035px"><svg width="40" height="12" viewBox="0 0 40 12"><path d="M2 6h35m-5-5 5 5-5 5" stroke="#fff" stroke-width="1.6" fill="none"/></svg></div>

<h2 class="section-title" style="top:2765px">Media <span>&amp; Impact</span></h2>
<div class="abs media-lead">Here is the media coverage for the programs and events that Dana oversaw.</div>

<div class="abs media-card" style="left:73px">
  <div class="media-head"><svg width="34" height="38" viewBox="0 0 34 38" fill="none" stroke="#3e66a8" stroke-width="2"><rect x="3" y="3" width="28" height="32" rx="2"/><path d="M9 11h16M9 17h16M9 23h16M9 29h10"/></svg>Articles</div>
  <div class="media-body"><b>March 2018</b>Attendees listening to a speaker at the Open Table Dinner Dialogue event</div>
  <div class="media-visual" style="background:linear-gradient(135deg,#a48a76,#6f7d93)" role="img" aria-label="Photo of attendees seated at dinner tables listening to a speaker"></div>
  <div class="load-more"><svg width="22" height="12" viewBox="0 0 22 12"><path d="M2 2l9 8 9-8" stroke="#5a80be" stroke-width="2.5" fill="none"/></svg>Load More</div>
</div>
<div class="abs media-card" style="left:433px">
  <div class="media-head"><svg width="40" height="36" viewBox="0 0 40 36" fill="none" stroke="#3e66a8" stroke-width="2"><rect x="3" y="3" width="34" height="24" rx="2"/><path d="M17 10v10l8-5z" fill="#3e66a8"/><path d="M12 33h16"/></svg>Videos</div>
  <div class="media-visual" style="height:200px;margin-top:18px;position:relative;background:linear-gradient(160deg,#8da3bf,#5e7a52 75%)" role="img" aria-label="Video still of a city plaza with people gathered on a lawn">
    <div class="play-btn"><svg width="18" height="20" viewBox="0 0 18 20"><path d="M3 2v16l13-8z" fill="#fff"/></svg></div>
  </div>
  <div class="load-more"><svg width="22" height="12" viewBox="0 0 22 12"><path d="M2 2l9 8 9-8" stroke="#5a80be" stroke-width="2.5" fill="none"/></svg>Load More</div>
</div>
<div class="abs media-card" style="left:793px">
  <div class="media-head"><svg width="36" height="36" viewBox="0 0 36 36" fill="none" stroke="#3e66a8" stroke-width="2"><circle cx="18" cy="18" r="15"/><circle cx="18" cy="16" r="4"/><path d="M11 24a10 10 0 1 1 14 0M15 30l3-10 3 10"/></svg>Podcasts</div>
  <div class="media-body">Dana welcoming volunteers to the annual College orientation week service event</div>
  <div class="media-visual" style="background:linear-gradient(180deg,#4a4f5c,#8a8f9c 60%,#2d3240)" role="img" aria-label="Photo of a speaker at a podium before a seated crowd in an auditorium"></div>
  <div class="load-more"><svg width="22" height="12" viewBox="0 0 22 12"><path d="M2 2l9 8 9-8" stroke="#5a80be" stroke-width="2.5" fill="none"/></svg>Load More</div>
</div>

<div class="abs contact-band"></div>
<h2 class="section-title" style="top:3505px">Contact</h2>
<div class="abs contact-item" style="left:150px;top:3598px;display:flex;gap:30px;width:780px">
  <svg width="56" height="72" viewBox="0 0 56 72" fill="none" stroke="#5a80be" stroke-width="2"><rect x="3" y="3" width="50" height="66" rx="3"/><text x="10" y="32" font-family="Montserrat,Arial,sans-serif" font-size="22" fill="#5a80be" stroke="none">$</text><path d="M28 20h18M28 28h18M10 44h36M10 52h36M10 60h24"/></svg>
  <div><b>Rates</b>Depending on the services requested, Dana offers an hourly rate, a package rate, or a retainer fee based on the scope and complexity of the project.</div>
</div>
<div class="abs contact-item" style="left:345px;top:3700px;display:flex;gap:30px;width:760px">
  <div><b>Book a complimentary consultation</b>Use the form below to tell Dana about your inquiry, and she will schedule a 30-minute meeting, phone call, or video chat to discuss your project outcomes.</div>
  <svg width="72" height="66" viewBox="0 0 72 66" fill="none" stroke="#5a80be" stroke-width="2"><rect x="3" y="8" width="46" height="40" rx="3"/><path d="M10 18h32M10 26h32M10 34h20"/><circle cx="57" cy="30" r="8"/><path d="M43 62c0-10 6-16 14-16s12 6 12 16"/></svg>
</div>

<div class="abs message" role="img" aria-label="Blue-tinted photo of volunteers gathered in a meeting room"></div>
<h2 class="section-title light" style="top:3980px">Send a Message</h2>
<div class="field" style="left:120px;top:4065px;width:310px">Your Name</div>
<div class="field" style="left:445px;top:4065px;width:310px">Your Email</div>
<div class="field" style="left:770px;top:4065px;width:310px">Your Subject</div>
<div class="field" style="left:120px;top:4128px;width:960px;height:130px">Message</div>
<div class="abs send-btn">Send Message</div>

<div class="abs footer-brand">
  <div class="brand-square"></div>
  <div class="brand-name" style="color:var(--navy)">Verdant Harbor Advisory</div>
</div>

<div class="abs footer-col" style="left:65px;width:180px">
  <h4>Quick Links</h4>
  Home<br>About<br>Services &amp; Testimonials<br>Media &amp; Impact<br>Contact
</div>
<div class="abs footer-col" style="left:275px;width:300px">
  <h4>Services</h4>
  Staff Professional Development<br>Community Partnership Development<br>Group Facilitation &amp; Leadership Training<br>Program Design, Implementation, &amp; Evaluation<br>Event Planning<br>Strategic Planning &amp; Visioning
</div>
<div class="abs footer-col" style="left:620px;width:230px">
  <h4>Contact</h4>
  <div class="row"><svg width="16" height="20" viewBox="0 0 16 20"><path d="M8 1a6 6 0 0 0-6 6c0 5 6 12 6 12s6-7 6-12a6 6 0 0 0-6-6z" fill="none" stroke="#2b3a5c" stroke-width="1.6"/><circle cx="8" cy="7" r="2" fill="#2b3a5c"/></svg><div>Verdant Harbor Advisory<br>48 Alder Row<br>Portsmouth, ME 03801</div></div>
  <div class="row"><svg width="16" height="16" viewBox="0 0 16 16"><path d="M4 1l3 3-2 2c1 2 3 4 5 5l2-2 3 3-2 3C7 15 1 9 1 3z" fill="none" stroke="#2b3a5c" stroke-width="1.5"/></svg><div>(555) 014-2290</div></div>
  <div class="row" style="margin-top:30px"><svg width="16" height="16" viewBox="0 0 16 16"><rect x="1" y="3" width="14" height="10" fill="none" stroke="#2b3a5c" stroke-width="1.5"/><path d="M1 3l7 6 7-6" fill="none" stroke="#2b3a5c" stroke-width="1.5"/></svg><div>hello@verdantharbor.org</div></div>
</div>
<div class="abs footer-col" style="left:875px;width:260px">
  <h4>Newsletter</h4>
  <div class="newsletter"><div>Enter Email Address</div><div>SIGN UP</div></div>
</div>

<div class="abs copyright">COPYRIGHT © 2019 VERDANT HARBOR ADVISORY. ALL RIGHTS RESERVED.</div>

</body>
</html>
```